Modern Warmth + Professional Balance Florfenicol Spray 5% packaging desgin

Size:40mm*40mm*154mm(H)
Product: Florfenicol Spray 5%(animal health)
Design Style: Please refer to the brand style of Pravelo and other international animal health companies to design a professional, clean, and trustworthy package for a pet topical spray. The information hierarchy should be clear, and the design should be suitable for the global market.

Target Market(s)

global market

Industry/Entity Type

veterinary drug

Colors
0054AA
0677BA
7BADD7
CADEEF
E8F1F8
0094D4
00A9DD
6FCCEA
C7EBF8
E9F6FB
00AB8E
00BBA5
67D7C9
C6EFE9
E9F9F6
59FF00
82FF00
B8FF75
E3FFCB
F4FFEA
EE7325
F08F49
F5BC92
FAE3D3
FDF4ED

```html
<!DOCTYPE html>
<html lang="en">
<head>
<meta charset="utf-8">
<title>Cutavera Florfenicol Spray 5% – Carton Front</title>
<link rel="stylesheet" href="https://fonts.googleapis.com/css2?family=Barlow:wght@500;600;700&family=Barlow+Semi+Condensed:wght@500;600&display=swap">
<style>
  :root {
    --stage: #9a9a9a;
    --carton: #e6e8e8;
    --brand-green: #66a028;
    --band-light: #a9c98a;
    --ink: #111111;
    --logo-navy: #0e1a4b;
    --art-top: #eef3e8;
    --art-bottom: #c5dcae;
  }
  * { margin: 0; padding: 0; box-sizing: border-box; }
  html, body { width: 1200px; height: 2346px; overflow: hidden; }
  body {
    background: var(--stage);
    position: relative;
    font-family: "Barlow", Arial, sans-serif;
    color: var(--ink);
  }
  .carton-front {
    position: absolute;
    left: 348px; top: 248px;
    width: 494px; height: 1886px;
    background: linear-gradient(180deg, #eceeee 0%, #e2e4e4 60%, #d8dada 100%);
  }
  .hero-art {
    position: absolute;
    left: 25px; top: 207px;
    width: 444px; height: 369px;
    background: linear-gradient(180deg, var(--art-top), var(--art-bottom));
    border-radius: 6px;
  }
  .name-band {
    position: absolute;
    left: 0; top: 576px;
    width: 100%; height: 186px;
    background: var(--brand-green);
    display: flex; align-items: center; justify-content: center;
  }
  .product-name {
    color: #f3f3f3;
    font-weight: 600;
    font-size: 77px;
    letter-spacing: 1px;
  }
  .product-name sup { font-size: 34px; vertical-align: 30px; margin-left: 2px; }
  .strength-band {
    position: absolute;
    left: 0; top: 762px;
    width: 100%; height: 103px;
    background: var(--band-light);
    display: flex; align-items: center; justify-content: center;
  }
  .strength-text {
    font-family: "Barlow Semi Condensed", Arial, sans-serif;
    font-weight: 600;
    font-size: 44px;
  }
  .species {
    position: absolute;
    left: 0; top: 1010px;
    width: 100%;
    text-align: center;
    font-weight: 500;
    font-size: 39px;
    line-height: 52px;
  }
  .paw-badge {
    position: absolute;
    left: 176px; top: 1140px;
    width: 156px; height: 156px;
  }
  .volume {
    position: absolute;
    left: 0; top: 1474px;
    width: 100%;
    text-align: center;
    font-weight: 700;
    font-size: 40px;
    font-family: "Barlow Semi Condensed", Arial, sans-serif;
  }
  .caution-box {
    position: absolute;
    left: 39px; top: 1558px;
    width: 414px; height: 91px;
    border: 3px solid var(--brand-green);
    font-family: "Barlow Semi Condensed", Arial, sans-serif;
    font-weight: 500;
    font-size: 30px;
    line-height: 38px;
    padding: 6px 0 0 17px;
  }
  .maker-name {
    position: absolute;
    left: 0; top: 1680px;
    width: 100%;
    text-align: center;
    color: var(--logo-navy);
    font-weight: 700;
    font-size: 62px;
    letter-spacing: 2px;
  }
</style>
</head>
<body>
  <main class="carton-front">
    <div class="hero-art" role="img" aria-label="Green line illustration of a dog, a cat and a rabbit standing on grass"></div>

    <div class="name-band">
      <h1 class="product-name">Cutavera<sup>™</sup></h1>
    </div>
    <div class="strength-band">
      <p class="strength-text">Florfenicol Spray 5%</p>
    </div>

    <p class="species">FOR DOGS, CATS,<br>FUR ANIMALS</p>

    <svg class="paw-badge" viewBox="0 0 156 156" aria-hidden="true">
      <circle cx="78" cy="78" r="75" fill="none" stroke="#66a028" stroke-width="4"/>
      <g fill="#66a028">
        <ellipse cx="40" cy="72" rx="13" ry="17" transform="rotate(-20 40 72)"/>
        <ellipse cx="62" cy="45" rx="13" ry="18" transform="rotate(-8 62 45)"/>
        <ellipse cx="94" cy="45" rx="13" ry="18" transform="rotate(8 94 45)"/>
        <ellipse cx="116" cy="72" rx="13" ry="17" transform="rotate(20 116 72)"/>
        <path d="M78 76c-16 0-34 20-34 36 0 12 10 15 19 13 6-1 10-4 15-4s9 3 15 4c9 2 19-1 19-13 0-16-18-36-34-36z"/>
      </g>
    </svg>

    <p class="volume">100ml</p>

    <div class="caution-box">CAUTION: Pregnant pets and<br>Collie should use it carefully</div>

    <p class="maker-name">NORVANE</p>
  </main>
</body>
</html>
```